Brochure design for moving and cleaning company

Hello

We need a NEW design of our brochure that we already have. Please check the brochure and give us a creative, professional and new design of it.

Here the brochure:

https://www.filecrate.example/s/ab3kd9x2lq7mzw1/0-1Brosura%20Trasko%20Mail4.9.17%20Trasko%202014%20Kopie%202.indd?dl=0

https://www.filecrate.example/s/pz8rt4vnw2hsy6e/2016%20Druck%201%20Brosura%202016%20Brosch%C3%BCre%20Druck.pdf?dl=0

I added the new text for the brochure and new logos and pictures.

Kind regards

T. Varnesh

Industry/Entity Type

Moving Company

Colors
ec1f27

Requirements
Must have
• http://lumofrex.example/red-brochure-template/red-brochure-template-red-and-white-corporate-brochure-template-vector-free-download-free/
Nice to have

```html
<!DOCTYPE html>
<html lang="de">
<head>
<meta charset="utf-8">
<title>Umzug &amp; Reinigung – Region</title>
<link href="https://fonts.googleapis.com/css2?family=Lato:ital,wght@0,700;0,900;1,700&display=swap" rel="stylesheet">
<style>
  :root {
    --blue-top: #4a9fe0;
    --blue-top-dark: #2b7fcc;
    --heading-blue: #1a72c4;
    --ink: #222222;
    --paper-edge: #e4e4e6;
    --paper: #ffffff;
    --navy: #142d5a;
    --ocean: #1b67b0;
    --wave-cyan: #a9dce8;
    --wave-mid: #2f87d2;
    --wave-deep: #1c58a6;
    --lime: #7cc242;
    --map-grey: #e2e4e8;
    --white: #ffffff;
  }
  * { box-sizing: border-box; margin: 0; padding: 0; }
  html, body { width: 1051px; height: 1200px; overflow: hidden; background: #cfcfd1; }
  body { font-family: "Lato", Arial, sans-serif; }

  .page {
    position: relative;
    width: 1051px;
    height: 1200px;
    overflow: hidden;
    background: linear-gradient(90deg, var(--paper-edge) 0%, var(--paper) 22%, var(--paper) 78%, var(--paper-edge) 100%);
  }
  .top-bar {
    position: absolute; left: 0; top: 0; width: 100%; height: 33px;
    background: linear-gradient(180deg, var(--blue-top) 0%, var(--blue-top-dark) 100%);
  }
  .headline {
    position: absolute; left: 71px; top: 80px; width: 900px;
    color: var(--heading-blue); font-weight: 700; font-size: 35px; line-height: 38px;
  }
  .tagline {
    position: absolute; left: 71px; top: 173px;
    color: var(--ink); font-weight: 700; font-style: italic; font-size: 33px; line-height: 40px;
  }
  .region-map {
    position: absolute; left: 331px; top: 232px; width: 655px; height: 333px;
    border-radius: 40px 60px 30px 80px;
    background: radial-gradient(ellipse at 50% 50%, #eef0f3 0%, var(--map-grey) 70%, #d8dbe2 100%);
  }
  .waves { position: absolute; left: 0; top: 0; width: 1051px; height: 1200px; }
  .claim {
    position: absolute; left: 0; top: 728px; width: 100%;
    text-align: center; color: var(--white); font-weight: 700; font-size: 33px; line-height: 35px;
  }
  .weather-strip { position: absolute; left: 41px; top: 840px; width: 970px; height: 123px; }
  .weather-icon {
    position: absolute; top: 865px; width: 104px; height: 78px; border-radius: 40px;
  }
  .weather-icon.sun { left: 180px; background: radial-gradient(circle, #ffd43a 0%, #f5a30f 45%, rgba(255,255,255,0) 70%); }
  .weather-icon.rain { left: 300px; background: linear-gradient(180deg, #8e9298 0%, #b6c4d2 60%, #e3eef5 100%); }
  .weather-icon.storm { left: 447px; background: linear-gradient(180deg, #b7bcc4 0%, #d6d9de 60%, #f4e7a8 100%); }
  .weather-icon.snow { left: 597px; background: linear-gradient(180deg, #dcecf4 0%, #b9dceb 60%, #e9f4f9 100%); }
  .weather-icon.mixed { left: 747px; background: linear-gradient(135deg, #ffcf3a 0%, #a7acb3 50%, #cfe4ef 100%); }
  .team-photo {
    position: absolute; top: 988px; width: 351px; height: 171px;
    border: 2px solid var(--white); border-radius: 20px;
  }
  .team-photo.packing { left: 151px; background: linear-gradient(135deg, #7a5a3c 0%, #b89878 45%, #4f8fa6 100%); }
  .team-photo.mounting { left: 545px; background: linear-gradient(135deg, #d8d2c8 0%, #c49e80 50%, #5a3e30 100%); }
</style>
</head>
<body>
<main class="page">
  <div class="top-bar"></div>

  <h1 class="headline">Die Hin- und Rückfahrt in dieser Region werden<br>dem Kunde nicht verrechnet.</h1>
  <p class="tagline">Somit sind wir stets Ihr Nachbar.</p>

  <div class="region-map" role="img" aria-label="Karte der Nordschweiz mit Kantonswappen von Basel, Aargau, Zürich, Schaffhausen, Thurgau, Zug, Luzern, Schwyz und Bern"></div>

  <svg class="waves" viewBox="0 0 1051 1200" aria-hidden="true">
    <defs>
      <linearGradient id="deepSea" x1="0" y1="0" x2="1" y2="0.3">
        <stop offset="0" stop-color="var(--navy)"/>
        <stop offset="1" stop-color="var(--ocean)"/>
      </linearGradient>
    </defs>
    <path d="M0,640 C200,565 420,560 620,585 C790,605 950,575 1051,540 L1051,760 L0,760 Z" fill="var(--wave-cyan)"/>
    <path d="M720,592 C850,585 960,565 1051,528" fill="none" stroke="var(--lime)" stroke-width="5"/>
    <path d="M0,672 C200,605 420,612 650,652 C820,682 950,662 1051,622 L1051,760 L0,760 Z" fill="var(--wave-mid)"/>
    <path d="M0,700 C200,652 400,662 650,702 C850,732 960,712 1051,690 L1051,780 L0,780 Z" fill="var(--wave-deep)"/>
    <path d="M0,705 C160,662 340,668 540,698 C640,712 720,714 800,712" fill="none" stroke="var(--lime)" stroke-width="7"/>
    <path d="M0,712 C200,675 400,686 650,718 C850,742 960,734 1051,718 L1051,1200 L0,1200 Z" fill="url(#deepSea)"/>
    <polygon class="strip-shape" points="41,963 82,840 1011,840 970,963" fill="var(--white)"/>
  </svg>

  <p class="claim">Organisation, Teamfähigkeit, Motivation und unser<br>konstruktiver Umgang mit dem Kunden, machen uns<br>für alle Aufträge und Wetter tauglich.</p>

  <div class="weather-icon sun" role="img" aria-label="Wettersymbol Sonne"></div>
  <div class="weather-icon rain" role="img" aria-label="Wettersymbol Regenwolke"></div>
  <div class="weather-icon storm" role="img" aria-label="Wettersymbol Gewitter"></div>
  <div class="weather-icon snow" role="img" aria-label="Wettersymbol Schnee"></div>
  <div class="weather-icon mixed" role="img" aria-label="Wettersymbol Sonne, Regen und Regenbogen"></div>

  <div class="team-photo packing" role="img" aria-label="Foto: zwei Mitarbeiter verpacken eine Statue in Folie"></div>
  <div class="team-photo mounting" role="img" aria-label="Foto: Mitarbeiter demontiert einen Kronleuchter auf einer Leiter"></div>
</main>
</body>
</html>
```